business card with logo Velmora Nails & Spa 2816 SW Quillan Ave Portland OR 97384

Would like to have a business card with our logo.
like bottle of polish with our logo or letter V on it
want something that first glance would let you know that it is a nail salon.
like the hands with polish bottle dripping.
like black or White back ground

Velmora Nails & Spa
(The Velvet Retreat)
2816 SW Quillan Ave
Portland, OR 97384
Call or Text: 1-503-555-0148
www.VelmoraNailsnSpa.example
Open 7 days a week.
After 7:00 PM is by appointment only.
Closed only on Thanksgiving & Christmas.

Target Market(s)

20%Man and 80%Woman 13-70

Industry/Entity Type

Business

Contact Information for Business Card

Elegant with Logo-Business name- address-phone-open days. closed day.

Font styles to use
Decorative
Script

Colors
000000

Requirements
Must have
• Logo and place for Technician Name
• Velmora Nails & Spa
• (The Velvet Retreat)
• 2816 SW Quillan Ave
• Portland, OR 97384
• Call or Text: 1-503-555-0148
• Open 7 days a week
• Closed only on Thanksgiving & Christmas.
• We accepted all major credit cards but prefer cash. Thank you
Nice to have
• Nail polish bottle with our Logo or letter V
Should not have
• too colorful

```html
<!DOCTYPE html>
<html lang="en">
<head>
<meta charset="utf-8">
<title>Velmora Nails &amp; Spa – Business Card</title>
<link rel="stylesheet" href="https://fonts.googleapis.com/css2?family=Open+Sans:wght@400;600&display=swap">
<style>
  :root {
    --bg: #2b2b2b;
    --card: #ffffff;
    --ink: #111111;
    --muted: #555555;
    --accent-red: #d0201f;
    --accent-green: #8dc63f;
    --badge: #eeeeee;
    --badge-edge: #cfcfcf;
    --rule: #bbbbbb;
  }
  html, body {
    margin: 0;
    width: 1200px;
    height: 1200px;
    overflow: hidden;
    background: var(--bg);
    font-family: "Open Sans", Arial, sans-serif;
  }
  .business-card {
    position: absolute;
    left: 300px;
    top: 75px;
    width: 600px;
    height: 1050px;
    background: var(--card);
    border-radius: 26px;
    overflow: hidden;
    color: var(--ink);
  }
  .polish-photo {
    position: absolute;
    right: 0;
    top: 40px;
    width: 180px;
    height: 560px;
    background: linear-gradient(180deg, #f6e2d6 0%, #f3d3c2 30%, #e0544a 62%, #c8181a 85%, #ffffff 100%);
    border-radius: 12px 0 0 12px;
  }
  .brand {
    position: absolute;
    left: 48px;
    top: 110px;
    width: 340px;
  }
  .brand-line {
    display: flex;
    align-items: center;
    gap: 12px;
  }
  .brand-dot {
    flex: none;
    width: 18px;
    height: 18px;
    border-radius: 50%;
    background: var(--accent-red);
  }
  .brand-name {
    font-size: 28px;
    font-weight: 600;
    color: var(--ink);
    white-space: nowrap;
  }
  .tagline {
    margin: 8px 0 0 30px;
    font-size: 20px;
    color: var(--accent-green);
  }
  .contact {
    position: absolute;
    left: 48px;
    top: 300px;
    width: 360px;
    font-size: 20px;
    line-height: 1.45;
  }
  .contact-row {
    display: flex;
    align-items: flex-start;
    gap: 12px;
    margin-bottom: 10px;
  }
  .contact-row svg { flex: none; margin-top: 4px; }
  .hours {
    position: absolute;
    right: 40px;
    top: 660px;
    text-align: right;
    font-size: 22px;
    line-height: 1.55;
  }
  .payment-title {
    position: absolute;
    right: 40px;
    top: 800px;
    font-size: 22px;
    color: var(--accent-red);
  }
  .payment-list {
    position: absolute;
    left: 40px;
    right: 40px;
    top: 860px;
    display: flex;
    justify-content: space-between;
    list-style: none;
    margin: 0;
    padding: 0;
  }
  .payment-item {
    display: flex;
    align-items: center;
    gap: 8px;
    font-size: 17px;
    font-weight: 600;
    color: var(--ink);
  }
  .payment-square {
    width: 16px;
    height: 16px;
    background: var(--badge);
    border: 1px solid var(--badge-edge);
  }
  .cash-note {
    position: absolute;
    right: 40px;
    top: 908px;
    font-size: 18px;
    color: var(--muted);
  }
  .technician {
    position: absolute;
    left: 40px;
    right: 40px;
    top: 970px;
    display: flex;
    align-items: flex-end;
    gap: 12px;
    font-size: 18px;
  }
  .technician-line {
    flex: 1;
    border-bottom: 1px solid var(--rule);
    height: 22px;
  }
</style>
</head>
<body>
  <main class="business-card">
    <div class="polish-photo" role="img" aria-label="Hand with red painted nails lifting a brush from a dripping red nail polish bottle"></div>

    <header class="brand">
      <div class="brand-line">
        <span class="brand-dot"></span>
        <span class="brand-name">Velmora Nails &amp; Spa</span>
      </div>
      <div class="tagline">(The Velvet Retreat)</div>
    </header>

    <section class="contact">
      <div class="contact-row">
        <svg width="18" height="24" viewBox="0 0 18 24" aria-hidden="true"><path d="M9 0C4 0 0 4 0 9c0 6 9 15 9 15s9-9 9-15c0-5-4-9-9-9z" fill="var(--accent-red)"/><circle cx="9" cy="9" r="3.5" fill="#fff"/></svg>
        <div>2816 SW Quillan Ave<br>Portland, OR 97384</div>
      </div>
      <div class="contact-row">
        <svg width="18" height="24" viewBox="0 0 18 24" aria-hidden="true"><rect x="2" y="1" width="14" height="22" rx="2.5" fill="none" stroke="var(--accent-red)" stroke-width="2"/><circle cx="9" cy="19" r="1.4" fill="var(--accent-red)"/></svg>
        <div>1-503-555-0148 (Call or Text)</div>
      </div>
      <div class="contact-row">
        <svg width="18" height="20" viewBox="0 0 20 20" aria-hidden="true"><g fill="none" stroke="var(--accent-red)" stroke-width="1.6"><circle cx="10" cy="10" r="8.5"/><ellipse cx="10" cy="10" rx="3.8" ry="8.5"/><line x1="1.5" y1="10" x2="18.5" y2="10"/></g></svg>
        <div>www.VelmoraNailsnSpa.example</div>
      </div>
    </section>

    <section class="hours">
      Open 7 days a week.<br>
      After 7:00 PM is by appointment only.<br>
      Closed only on Thanksgiving &amp; Christmas
    </section>

    <div class="payment-title">We Accept All major credit cards:</div>

    <ul class="payment-list">
      <li class="payment-item"><span class="payment-square"></span>Varda</li>
      <li class="payment-item"><span class="payment-square"></span>Mintcard</li>
      <li class="payment-item"><span class="payment-square"></span>Amerigo Pay</li>
      <li class="payment-item"><span class="payment-square"></span>Dexpath</li>
    </ul>

    <div class="cash-note">but prefer cash. Thank you</div>

    <div class="technician">
      <span>Technician:</span>
      <span class="technician-line"></span>
    </div>
  </main>
</body>
</html>
```